Kickass billboard for motorway

We take dented trucks - clue is in the name.
We have a 45ft billboard we're looking to design constructed from an old trailer we own (so we can be as creative as possible).
We provide a van buying service, being one of the only companies in the UK with the facilities to recover faulty, damaged and broken vans - from small car derived vans to large trucks and lorries.
ur niche in the market is different to car buying services, as buying and selling cars is often an emotionally driven process, whereas people often see and treat vans purely as a tool. There are alternatives to a car, public transport etc, but not to a work van - so people go out straight away and replace them immediately, often leaving the old broken van to sit on their drive or in their unit.
Looking to start building a brand asset bank.
Feel free to check out our website to get a feel for what we do:
Wetakedentedtrucks.co.uk

Target Market(s)

Van owners/drivers & fleet managers

Industry/Entity Type

Automotive

Font styles to use
Sans Serif

Colors
34a7d8

Requirements
Must have
• Eye-catching - very eye-catching.
We want to advertise the fact we collect vehicles for free.
We pay instantly upon arrival.
Our phone number 0161 473 2046
Our website www.wetakedentedtrucks.co.uk
Nice to have
• 3d elements - we have the ability to get 3d props for the billboard including damaged vans etc.

```html
<!DOCTYPE html>
<html lang="en">
<head>
<meta charset="utf-8">
<title>We Take Dented Trucks – Motorway Billboard</title>
<link rel="stylesheet" href="https://fonts.googleapis.com/css2?family=Montserrat:ital,wght@0,700;0,800;0,900;1,800;1,900&display=swap">
<style>
  :root {
    --brand-blue: #34a7d8;
    --panel-blue: #4aabdf;
    --sun-yellow: #fcea00;
    --ink: #1c1a1b;
    --paper: #ffffff;
    --stage: #cfcfcf;
    --stage-dark: #8e8e8e;
  }
  * { margin: 0; padding: 0; box-sizing: border-box; }
  html, body {
    width: 1200px; height: 1135px; overflow: hidden;
  }
  body {
    background: radial-gradient(ellipse at 40% 40%, #e4e4e4 0%, var(--stage) 55%, var(--stage-dark) 100%);
    font-family: "Montserrat", Arial, sans-serif;
    position: relative;
  }
  .billboard {
    position: absolute;
    left: 30px; top: 407px;
    width: 1140px; height: 320px;
    background: var(--paper);
    box-shadow: 0 6px 18px rgba(0,0,0,0.35);
    overflow: hidden;
  }
  .billboard-shapes {
    position: absolute; inset: 0;
  }
  .billboard-text { position: absolute; white-space: nowrap; }

  .phone {
    left: 30px; top: 20px;
    display: flex; align-items: center; gap: 10px;
    font-weight: 800; font-size: 53px; letter-spacing: -0.5px;
    color: var(--ink); line-height: 1;
  }
  .phone svg { width: 34px; height: 34px; }

  .brand {
    left: 32px; top: 136px;
    display: flex; align-items: center; gap: 14px;
  }
  .brand-dot {
    width: 40px; height: 40px; border-radius: 50%;
    background: var(--brand-blue);
  }
  .brand-name {
    font-weight: 700; font-size: 35px; color: var(--paper);
    letter-spacing: -0.5px; line-height: 1;
  }

  .promise {
    left: 28px; top: 247px;
    font-style: italic; font-weight: 900; font-size: 23.5px;
    color: var(--ink); letter-spacing: -0.2px; line-height: 1;
  }
  .promise .accent { color: var(--brand-blue); }

  .website {
    left: 80px; top: 282px;
    display: flex; align-items: center; gap: 8px;
    font-style: italic; font-weight: 800; font-size: 17.5px;
    color: var(--ink); line-height: 1;
  }
  .website svg { width: 20px; height: 20px; }

  .headline {
    left: 606px; width: 534px; top: 22px;
    text-align: center;
    font-style: italic; font-weight: 900; font-size: 43px;
    line-height: 46px; color: var(--paper); letter-spacing: -0.3px;
  }

  .valuation {
    left: 654px; top: 133px;
    width: 372px; height: 50px; border-radius: 25px;
    background: var(--ink); color: var(--paper);
    display: flex; align-items: center; justify-content: center;
    font-style: italic; font-weight: 900; font-size: 26px; letter-spacing: 0.2px;
  }

  .collection {
    left: 606px; width: 534px; top: 212px;
    text-align: center;
    font-style: italic; font-weight: 900; font-size: 33px;
    line-height: 37px; color: var(--ink); letter-spacing: -0.3px;
  }
</style>
</head>
<body>
  <main class="billboard" aria-label="Motorway billboard for We Take Dented Trucks">
    <svg class="billboard-shapes" viewBox="0 0 1140 320" width="1140" height="320" aria-hidden="true">
      <defs>
        <clipPath id="offer-panel">
          <path d="M606,0 H1140 V320 H606 C530,320 486,244 486,160 C486,76 530,0 606,0 Z"/>
        </clipPath>
      </defs>
      <g clip-path="url(#offer-panel)">
        <rect class="offer-top" x="480" y="0" width="660" height="160" fill="var(--panel-blue)"/>
        <rect class="offer-bottom" x="480" y="160" width="660" height="160" fill="var(--sun-yellow)"/>
      </g>
      <path class="brand-band" d="M-10,90 H503 A68,68 0 0 1 503,226 H-10 Z"
            fill="var(--ink)" stroke="var(--paper)" stroke-width="4"/>
    </svg>

    <div class="billboard-text phone">
      <svg viewBox="0 0 24 24" aria-hidden="true">
        <path d="M6.6 10.8c1.4 2.8 3.8 5.1 6.6 6.6l2.2-2.2c.3-.3.7-.4 1-.2 1.1.4 2.3.6 3.6.6.6 0 1 .4 1 1V20c0 .6-.4 1-1 1C10.6 21 3 13.4 3 4c0-.6.4-1 1-1h3.5c.6 0 1 .4 1 1 0 1.3.2 2.5.6 3.6.1.3 0 .7-.2 1z" fill="var(--brand-blue)"/>
        <path d="M14.5 2.5a7 7 0 0 1 7 7M14.5 6a3.5 3.5 0 0 1 3.5 3.5" fill="none" stroke="var(--brand-blue)" stroke-width="1.8" stroke-linecap="round"/>
      </svg>
      <span>0161 473 2046</span>
    </div>

    <div class="billboard-text brand">
      <span class="brand-dot" aria-hidden="true"></span>
      <span class="brand-name">wetakedentedtrucks</span>
    </div>

    <p class="billboard-text promise">WE PAY INSTANTLY <span class="accent">UPON ARRIVAL</span></p>

    <p class="billboard-text website">
      <svg viewBox="0 0 24 24" aria-hidden="true">
        <circle cx="12" cy="12" r="10.5" fill="none" stroke="var(--ink)" stroke-width="1.4"/>
        <circle cx="12" cy="12" r="7.5" fill="var(--brand-blue)"/>
        <path d="M4.5 12h15M12 4.5v15M6 8h12M6 16h12M12 4.5c-3 3-3 12 0 15M12 4.5c3 3 3 12 0 15" fill="none" stroke="var(--paper)" stroke-width="0.9"/>
      </svg>
      <span>www.wetakedentedtrucks.co.uk</span>
    </p>

    <h1 class="billboard-text headline">SELL YOUR VAN<br>IN ANY CONDITION</h1>

    <div class="billboard-text valuation">GET A FREE VALUATION</div>

    <p class="billboard-text collection">WE COLLECT VEHICLES<br>FOR FREE</p>
  </main>
</body>
</html>
```